Desk Allies Business Card

Contact Information for Business Card

Janne Voutilainen
Managing Director

3/47 Brindle Street Mitchell ACT 2911

Tel: +61 02 6257 3140
Mob: +61 0427 315 846

Email: janne@deskallies.com.au
Web: www.deskallies.com.au

Colors

Designer to choose colors to be used in the design.

Requirements
Must have
• Logo, Name, Title, Address, Telephone, Mobile, Email Address and Website
• "Desk Ally International Pty Ltd"

```html
<!DOCTYPE html>
<html lang="en">
<head>
<meta charset="utf-8">
<title>Desk Allies Business Card</title>
<link href="https://fonts.googleapis.com/css2?family=Open+Sans:wght@400;600;700&display=swap" rel="stylesheet">
<style>
  :root {
    --backdrop: #3a3330;
    --card: #141416;
    --card-edge: #202024;
    --brand-blue: #2f86d6;
    --text-light: #e6e6e6;
    --text-muted: #b8b8b8;
    --silver: #c9c9c9;
  }
  * { box-sizing: border-box; margin: 0; padding: 0; }
  html, body {
    width: 1200px; height: 864px; overflow: hidden;
    background: var(--backdrop);
    font-family: "Open Sans", sans-serif;
  }
  .canvas { position: relative; width: 1200px; height: 864px; }
  .card {
    position: absolute; width: 560px; height: 320px;
    background: var(--card);
    border: 1px solid var(--card-edge);
    box-shadow: 0 14px 30px rgba(0,0,0,.45);
  }
  .card--front { left: 80px; top: 100px; }
  .card--back { left: 560px; top: 444px; }

  /* front */
  .front-brand {
    position: absolute; left: 60px; top: 92px;
    display: flex; align-items: center; gap: 18px;
  }
  .front-brand__dot {
    width: 64px; height: 64px; border-radius: 50%;
    background: var(--silver);
  }
  .front-brand__name {
    font-size: 46px; font-weight: 600; color: var(--silver); letter-spacing: .5px;
  }
  .front-web {
    position: absolute; left: 60px; top: 228px;
    font-size: 15px; letter-spacing: 3.5px; color: var(--text-muted);
  }

  /* back */
  .back-brand {
    position: absolute; left: 34px; top: 136px;
    display: flex; align-items: center; gap: 10px;
  }
  .back-brand__dot {
    width: 30px; height: 30px; border-radius: 50%;
    background: var(--brand-blue);
  }
  .back-brand__name {
    font-size: 24px; font-weight: 600; color: var(--brand-blue);
    text-transform: uppercase; letter-spacing: .3px;
  }
  .divider {
    position: absolute; left: 272px; top: 60px; width: 1px; height: 200px;
    background: linear-gradient(to bottom, transparent, #d8d8d8 50%, transparent);
  }
  .contact {
    position: absolute; left: 292px; top: 66px; color: var(--text-light);
  }
  .contact__name {
    font-size: 19px; font-weight: 700; color: var(--brand-blue);
    text-transform: uppercase; line-height: 1.1;
  }
  .contact__title {
    font-size: 17px; font-weight: 700; text-transform: uppercase;
    line-height: 1.25; margin-bottom: 8px;
  }
  .contact__company, .contact__address {
    font-size: 11.5px; line-height: 1.45; color: var(--text-muted);
  }
  .contact__list { list-style: none; margin-top: 6px; }
  .contact__item {
    display: flex; align-items: center; gap: 8px;
    font-size: 14.5px; line-height: 1.45;
  }
  .contact__icon { width: 14px; height: 14px; flex: none; fill: var(--brand-blue); }
  .contact__icon--none { visibility: hidden; }
</style>
</head>
<body>
<main class="canvas">

  <section class="card card--front" aria-label="Business card front">
    <div class="front-brand">
      <span class="front-brand__dot"></span>
      <span class="front-brand__name">Desk Allies</span>
    </div>
    <p class="front-web">WWW.DESKALLIES.COM.AU</p>
  </section>

  <section class="card card--back" aria-label="Business card back">
    <div class="back-brand">
      <span class="back-brand__dot"></span>
      <span class="back-brand__name">Desk Allies</span>
    </div>

    <div class="divider"></div>

    <div class="contact">
      <p class="contact__name">Janne Voutilainen</p>
      <p class="contact__title">Managing Director</p>
      <p class="contact__company">Desk Ally International Pty Ltd</p>
      <p class="contact__address">3/47 Brindle Street Mitchell ACT 2911</p>
      <ul class="contact__list">
        <li class="contact__item">
          <svg class="contact__icon" viewBox="0 0 16 16" aria-hidden="true"><path d="M3 1h3l1.5 4-2 1.3a9 9 0 0 0 4.2 4.2L11 8.5l4 1.5v3a2 2 0 0 1-2 2C6.4 15 1 9.6 1 3a2 2 0 0 1 2-2z"/></svg>
          <span>+61 02 6257 3140</span>
        </li>
        <li class="contact__item">
          <svg class="contact__icon" viewBox="0 0 16 16" aria-hidden="true"><path d="M4.5 0h7A1.5 1.5 0 0 1 13 1.5v13a1.5 1.5 0 0 1-1.5 1.5h-7A1.5 1.5 0 0 1 3 14.5v-13A1.5 1.5 0 0 1 4.5 0zM5 2v10h6V2zm3 11a1 1 0 1 0 0 2 1 1 0 0 0 0-2z"/></svg>
          <span>+61 0427 315 846</span>
        </li>
        <li class="contact__item">
          <svg class="contact__icon" viewBox="0 0 16 16" aria-hidden="true"><path d="M1 3h14v10H1zm1.5 1.5L8 9l5.5-4.5z" fill-rule="evenodd"/></svg>
          <span>janne@deskallies.com.au</span>
        </li>
        <li class="contact__item">
          <svg class="contact__icon" viewBox="0 0 16 16" aria-hidden="true"><circle cx="8" cy="8" r="7"/></svg>
          <span>www.deskallies.com.au</span>
        </li>
      </ul>
    </div>
  </section>

</main>
</body>
</html>
```